Book Cover Design Project

I would like a book cover designed for a book entitled: Bright Days Ahead: Finding the Right Cosmetic Dentist
The target audience is those patients interested in cosmetic dentistry. Generally those would be people over 45, with above average income, but the cover should have more universal appeal.
The book was written by
Raymond T. Oakes, DDS, FSFDP
Fellow in the Society of Family Dental Practice
(that's me)
The book will be distributed as an ebook for free to patients and potential patients interested in cosmetic dentistry.

```html
<!DOCTYPE html>
<html lang="en">
<head>
<meta charset="utf-8">
<title>Bright Days Ahead: Finding the Right Cosmetic Dentist</title>
<link rel="stylesheet" href="https://fonts.googleapis.com/css2?family=Fira+Sans:wght@400;600;700&display=swap">
<style>
  :root {
    --backdrop: #2b2b2d;
    --navy-top: #06264a;
    --blue-bottom: #0078bf;
    --leaf-green: #0f9444;
    --paper: #ffffff;
    --credit-blue: #1a7cc1;
    --skin-light: #e2a88a;
    --skin-deep: #b9735a;
  }
  html, body {
    margin: 0;
    padding: 0;
    width: 1200px;
    height: 960px;
    overflow: hidden;
    background: var(--backdrop);
  }
  .book-cover {
    position: absolute;
    left: 260px;
    top: 40px;
    width: 680px;
    height: 880px;
    overflow: hidden;
    font-family: "Fira Sans", sans-serif;
  }
  .cover-art {
    position: absolute;
    inset: 0;
    width: 100%;
    height: 100%;
  }
  .cover-title {
    position: absolute;
    top: 52px;
    left: 0;
    width: 100%;
    margin: 0;
    text-align: center;
    color: var(--paper);
    font-weight: 700;
    font-size: 58px;
    line-height: 1;
    font-variant: small-caps;
    letter-spacing: 0.5px;
  }
  .cover-subtitle {
    position: absolute;
    top: 122px;
    left: 0;
    width: 100%;
    margin: 0;
    text-align: center;
    color: var(--paper);
    font-weight: 400;
    font-size: 26px;
    letter-spacing: 1.3px;
    line-height: 1;
  }
  .author-credit {
    position: absolute;
    top: 820px;
    left: 0;
    width: 100%;
    margin: 0;
    text-align: center;
    color: var(--credit-blue);
    font-size: 13px;
    line-height: 18px;
  }
</style>
</head>
<body>
  <main class="book-cover">
    <svg class="cover-art" viewBox="0 0 612 792" preserveAspectRatio="none" aria-hidden="false">
      <defs>
        <linearGradient id="sky-gradient" x1="0" y1="0" x2="0" y2="1">
          <stop offset="0" stop-color="var(--navy-top)"/>
          <stop offset="1" stop-color="var(--blue-bottom)"/>
        </linearGradient>
        <radialGradient id="smile-tones" cx="0.5" cy="0.5" r="0.6">
          <stop offset="0" stop-color="var(--skin-light)"/>
          <stop offset="1" stop-color="var(--skin-deep)"/>
        </radialGradient>
      </defs>
      <rect class="cover-ground" width="612" height="792" fill="url(#sky-gradient)"/>
      <path class="green-sweep" fill="var(--leaf-green)"
            d="M0,446 C60,608 200,676 360,684 C480,692 570,708 612,740 L612,792 L0,792 Z"/>
      <path class="white-sweep" fill="var(--paper)"
            d="M0,466 C60,626 200,694 360,702 C480,710 570,728 612,764 L612,792 L0,792 Z"/>
      <path class="smile-heart" role="img" aria-label="Close-up photo of a smiling mouth with bright white teeth, framed in a heart"
            fill="url(#smile-tones)" stroke="var(--paper)" stroke-width="14" stroke-linejoin="round"
            d="M306,279 C282,198 182,168 112,213 C40,260 58,372 120,442 C180,510 262,570 306,630 C350,570 432,510 492,442 C554,372 572,260 500,213 C430,168 330,198 306,279 Z"/>
    </svg>

    <h1 class="cover-title">Bright Days Ahead</h1>
    <p class="cover-subtitle">Finding the Right Cosmetic Dentist</p>

    <p class="author-credit">
      Raymond T. Oakes, DDS, FSFDP<br>
      Fellow in the Society of Family Dental Practice
    </p>
  </main>
</body>
</html>
```